Bay & Meadow Property Services Tri-fold sales & marketing brochure

We need a tri-fold brochure that describes our three lines of business and the various services within each line to use in sales and marketing efforts.
See website for additional background info:
https://halvernq7.example-host.com/

Target Market(s)

Real Estate Investors & owners in Residential Rental, Short-term Rentals, and Mini/Maxi Storage Rental markets

Requirements
Must have
• See attached logo, use color scheme & font styles to match. Make sure to utilize photos to enhance look/feel.

```html
<!DOCTYPE html>
<html lang="en">
<head>
<meta charset="utf-8">
<title>Bay &amp; Meadow Property Services – Tri-fold Brochure</title>
<link href="https://fonts.googleapis.com/css2?family=Roboto:wght@400;700;900&family=Roboto+Condensed:wght@400;700&family=Bebas+Neue&family=Kaushan+Script&display=swap" rel="stylesheet">
<style>
:root{
  --ink:#1f1d1e;
  --dark:#231f20;
  --teal:#1aa3c6;
  --teal-deep:#2aa6b6;
  --sea:#5cb9bf;
  --pale:#eaf2d3;
  --cream:#f4f4dc;
  --rule:#b9d9d6;
  --white:#ffffff;
}
*{margin:0;padding:0;box-sizing:border-box}
html,body{width:901px;height:1200px;overflow:hidden;background:var(--white)}
body{position:relative;font-family:"Roboto",Arial,sans-serif;color:var(--ink)}
.sheet{position:absolute;left:124px;width:651px;height:461px;border:1px solid var(--ink);background:var(--white);overflow:hidden}
.sheet--outside{top:108px}
.sheet--inside{top:628px}
.panel{position:absolute;top:0;height:100%}
.panel--left{left:0;width:216px}
.panel--mid{left:216px;width:218px}
.panel--right{left:434px;width:217px}

.card{position:absolute;left:12px;top:15px;width:194px;height:433px;border:1px solid var(--rule);overflow:hidden;background:var(--white)}
.card__dark{position:absolute;left:0;right:0;bottom:0;background:var(--dark)}

.headline{font-weight:900;line-height:1.1;text-transform:uppercase}
.body-copy{font-family:"Roboto Condensed",Arial,sans-serif;font-size:7px;line-height:8.5px;color:var(--ink)}
.accent{color:var(--teal)}

/* bullet lists */
.services{list-style:none;position:absolute;left:16px;right:12px}
.services li{display:flex;align-items:center;gap:6px;color:var(--white);border-bottom:1px solid #9a9a9a}
.services li:last-child{border-bottom:none}
.bullet{flex:none;width:12px;height:12px;border-radius:50%;background:var(--teal);border:2px solid var(--white)}

/* outside left */
.intro-title{position:absolute;left:17px;top:12px;font-size:19px;line-height:21px}
.intro-copy{position:absolute;left:17px;top:112px;width:165px}
.intro-copy p+p{margin-top:8.5px}
.why-title{position:absolute;left:17px;font-size:13px;font-weight:700;color:var(--teal)}
.why-list li{height:28.5px;font-size:10.5px}

/* outside mid */
.panel--contact{background:linear-gradient(180deg,var(--pale) 0%,#d3e9d4 30%,#8ccac6 62%,var(--teal-deep) 100%);text-align:center}
.contact-title{position:absolute;left:0;right:0;top:22px;font-size:21px;line-height:23px}
.tick{position:absolute;left:160px;top:58px}
.contact-sub{position:absolute;left:0;right:0;top:88px;font-size:11px;line-height:14px}
.couple-photo{position:absolute;left:6px;top:118px;width:206px;height:150px;border-radius:50% 50% 40% 40%;background:radial-gradient(ellipse at center,#cfe3dc 0%,#b4d9d3 55%,rgba(150,205,200,0) 100%)}
.review-badge{position:absolute;left:66px;top:275px;width:86px;height:22px;border-radius:11px;background:var(--white);opacity:.9}
.stars{position:absolute;left:0;right:0;top:304px;font-size:11px;letter-spacing:3px;color:var(--white)}
.phone{position:absolute;left:28px;top:338px;width:163px;height:32px;border-radius:16px;background:var(--cream);box-shadow:2px 3px 4px rgba(0,0,0,.25);font-size:19.5px;font-weight:700;line-height:32px}
.address{position:absolute;left:0;right:0;top:380px;font-size:9.3px;line-height:14px;color:var(--ink)}
.web{position:absolute;left:0;right:0;font-size:13px;font-weight:700;color:var(--white);text-align:center;white-space:nowrap}
.panel--contact .web{top:413px}

/* outside right / cover */
.brand{position:absolute;left:36px;top:24px;display:flex;align-items:center;gap:8px}
.brand__dot{width:42px;height:42px;border-radius:50%;background:var(--teal)}
.brand__name{font-size:15px;font-weight:700;color:var(--ink);line-height:17px}
.cover-title{position:absolute;left:0;right:0;top:95px;text-align:center;font-size:20px;line-height:19px}
.cover-script{position:absolute;left:0;right:0;top:150px;text-align:center;font-family:"Kaushan Script",cursive;font-size:34px;color:var(--teal)}
.cover-art{position:absolute;left:0;top:180px}
.panel--right .web{top:424px}

/* inside */
.sector-title{position:absolute;left:17px;top:14px;font-size:14px;line-height:16px;font-weight:700}
.sector-copy{position:absolute;left:17px;top:55px;width:170px}
.sector-photo{position:absolute;left:0;right:0;top:106px;height:120px}
.services-title{position:absolute;left:17px;top:252px;font-size:14px;line-height:16px;font-weight:700}
.service-list{top:293px}
.service-list li{height:28px;font-size:8.5px;line-height:10px}
.service-list--tall li{height:30px}

.panel--str{background:linear-gradient(180deg,var(--pale) 0%,var(--pale) 26%,#8fcfcd 60%,var(--teal-deep) 100%)}
.panel--str .sector-title{left:25px;top:37px}
.panel--str .sector-copy{left:25px;top:71px;width:182px}
.panel--str .sector-photo{top:121px}
.panel--str .services-title{left:25px;top:256px;color:var(--white)}
.panel--str .service-list{left:25px;right:28px;top:296px}
.panel--str .service-list li{color:var(--white);border-bottom-color:rgba(255,255,255,.6)}
.panel--str .service-list li:last-child{border-bottom:none}
.panel--str .bullet{background:var(--white);border-color:var(--teal)}
.tagline{position:absolute;left:0;right:0;top:424px;text-align:center;font-family:"Bebas Neue",sans-serif;font-size:22px;color:var(--cream)}
.card--inside .sector-title{top:22px}
.card--inside .sector-copy{top:56px}
.card--inside .sector-photo{top:106px}
</style>
</head>
<body>

<section class="sheet sheet--outside">
  <div class="panel panel--left">
    <div class="card">
      <h2 class="headline intro-title">Grounded<br>in expertise.<br><span class="accent">Built for<br>performance.</span></h2>
      <div class="body-copy intro-copy">
        <p>At Bay &amp; Meadow Property Services, we combine boots-on-the-ground experience with next-level strategy to unlock value in every square foot. Whether it’s transforming a vacant lot into a high-performing storage facility or managing a multi-unit vacation-rental portfolio remotely, we specialize in making real estate work smarter—for you.</p>
        <p>We are operators, builders, and investors who understand the intricacies of today’s most lucrative real estate verticals: Short-Term Rentals (STRs), Residential Rentals, and Mini/Maxi Storage Facilities. We don’t just offer services—we deliver outcomes that scale wealth, reduce risk, and free up your time.</p>
      </div>
      <div class="card__dark" style="top:236px">
        <h3 class="why-title" style="top:22px">WHY WORK WITH US?</h3>
        <ul class="services why-list" style="top:40px">
          <li><span class="bullet"></span>End-to-End Execution</li>
          <li><span class="bullet"></span>Niche Market Focus</li>
          <li><span class="bullet"></span>Proven Track Record</li>
          <li><span class="bullet"></span>System-Driven Efficiency</li>
          <li><span class="bullet"></span>Flexible Partnership</li>
        </ul>
      </div>
    </div>
  </div>

  <div class="panel panel--mid panel--contact">
    <h2 class="headline contact-title">Real estate,<br>done right</h2>
    <svg class="tick" width="26" height="20" viewBox="0 0 26 20" aria-hidden="true"><path d="M2 11 L9 17 L24 3" fill="none" stroke="var(--teal)" stroke-width="2.5" stroke-linecap="round"/></svg>
    <p class="contact-sub">Let’s build something valuable,<br>together.</p>
    <div class="couple-photo" role="img" aria-label="Photo of a smiling couple looking at a tablet together on a sofa"></div>
    <div class="review-badge" role="img" aria-label="Review rating badge"></div>
    <div class="stars" aria-label="Five star rating">★★★★★</div>
    <div class="phone">(555) 014-2290</div>
    <p class="address">410 Linden Row, Harbor Falls, WI 54000<br>info@bayandmeadowservices.com</p>
    <p class="web">halvernq7.example-host.com</p>
  </div>

  <div class="panel panel--right">
    <div class="brand">
      <span class="brand__dot"></span>
      <span class="brand__name">Bay &amp; Meadow<br>Property Services</span>
    </div>
    <h1 class="headline cover-title">Where expertise<br>meets<br>exceptional</h1>
    <p class="cover-script">Returns</p>
    <svg class="cover-art" width="217" height="281" viewBox="0 0 217 281">
      <defs>
        <linearGradient id="suburb" x1="0" y1="0" x2="1" y2="1">
          <stop offset="0" stop-color="#6f9a52"/>
          <stop offset=".5" stop-color="#8a9a78"/>
          <stop offset="1" stop-color="#4f7a3c"/>
        </linearGradient>
      </defs>
      <path d="M0 190 C10 195 30 200 60 205 C120 215 190 190 217 150 L217 281 L0 281 Z" fill="var(--teal)"/>
      <g role="img" aria-label="Aerial photo of a green suburban neighbourhood">
        <path d="M0 15 C40 5 70 10 95 25 C70 60 65 130 100 190 C60 200 25 198 0 190 Z" fill="url(#suburb)"/>
        <path d="M217 0 L217 150 C190 185 150 205 125 200 C95 150 100 60 150 25 C175 10 200 3 217 0 Z" fill="url(#suburb)"/>
      </g>
    </svg>
    <p class="web">halvernq7.example-host.com</p>
  </div>
</section>

<section class="sheet sheet--inside">
  <div class="panel panel--left">
    <div class="card card--inside">
      <h2 class="sector-title accent">RESIDENTIAL RENTAL<br>REAL ESTATE SECTOR</h2>
      <p class="body-copy sector-copy">The residential rental sector is a cornerstone of the broader real estate market, characterized by its diversity of options ranging from urban apartments to suburban single-family homes. This sector caters to a wide demographic, driven by factors.</p>
      <div class="sector-photo" role="img" aria-label="Photo of a hand holding glowing property management icons over a desk" style="background:linear-gradient(135deg,#0d3b44 0%,#1f7f86 55%,#0f3037 100%)"></div>
      <div class="card__dark" style="top:226px">
        <h3 class="services-title accent" style="top:26px">RESIDENTIAL<br>RENTAL SERVICES</h3>
        <ul class="services service-list" style="top:66px">
          <li><span class="bullet"></span>Market Research &amp; Feasibility Analysis</li>
          <li><span class="bullet"></span>Off-Market Property Sourcing</li>
          <li><span class="bullet"></span>Investment Matching</li>
          <li><span class="bullet"></span>Due Diligence Support</li>
          <li><span class="bullet"></span>Redevelopment Potential Identification</li>
        </ul>
      </div>
    </div>
  </div>

  <div class="panel panel--mid panel--str">
    <h2 class="sector-title">SHORT-TERM RENTAL<br>REAL ESTATE SECTOR</h2>
    <p class="body-copy sector-copy">This sector is particularly attractive due to its flexibility in pricing and the ability to generate higher per-night revenues compared to long-term rentals. Popular platforms allow owners to set dynamic pricing. And available market information allow owners to set demand-driven pricing.</p>
    <div class="sector-photo" role="img" aria-label="Photo of a hand passing house keys to another open hand" style="background:linear-gradient(135deg,#2b2521 0%,#5a4638 50%,#c9a88a 100%)"></div>
    <h3 class="services-title">SHORT-TERM<br>RENTAL SERVICES</h3>
    <ul class="services service-list service-list--tall">
      <li><span class="bullet"></span>Locating STR Project / Investment Opportunities</li>
      <li><span class="bullet"></span>ROI &amp; Occupancy Forecasting</li>
      <li><span class="bullet"></span>Off-Market Sourcing</li>
      <li><span class="bullet"></span>Market Positioning &amp; Audience Targeting</li>
    </ul>
    <p class="tagline">EXIT SMART, REINVEST STRONG</p>
  </div>

  <div class="panel panel--right">
    <div class="card card--inside">
      <h2 class="sector-title accent">MINI &amp; MAXI STORAGE<br>REAL ESTATE SECTOR</h2>
      <p class="body-copy sector-copy">Mini storage facilities, offering compact, secure units, cater to individuals and small businesses seeking space-efficient solutions for personal belongings, documents, or inventory.</p>
      <div class="sector-photo" role="img" aria-label="Aerial photo of rows of blue-roofed storage unit buildings" style="background:linear-gradient(160deg,#6e8f52 0%,#7a9cb0 30%,#5c7f98 65%,#3f4a55 100%)"></div>
      <div class="card__dark" style="top:226px">
        <h3 class="services-title accent" style="top:26px">STORAGE FACILITY<br>SERVICES</h3>
        <ul class="services service-list service-list--tall" style="top:64px">
          <li><span class="bullet"></span>Locating Project / Investment Opportunities</li>
          <li><span class="bullet"></span>Feasibility Studies &amp; Market Analysis</li>
          <li><span class="bullet"></span>Off-Market Site Sourcing</li>
          <li><span class="bullet"></span>Investment Planning &amp; Portfolio Strategy</li>
        </ul>
      </div>
    </div>
  </div>
</section>

</body>
</html>
```